Redesign of Business Cards to Update them!

We want a full overhaul of our business cards! We have a design that is almost 5 years old and it needs to be updated to be current

Address is 457 Calloway Court Suite B Cedar Hollow CA 92481
PH: 9094417382
Tindlebox.com

Hours M-F 9AM-5PM
Sat and Sun by Appointment

```html
<!DOCTYPE html>
<html lang="en">
<head>
<meta charset="utf-8">
<title>Tindlebox Business Card</title>
<link rel="stylesheet" href="https://fonts.googleapis.com/css2?family=Josefin+Sans:wght@600;700&family=Poppins:wght@400;500&family=Oswald:wght@500&display=swap">
<style>
  :root {
    --red: #ec1c24;
    --black: #0d0d0d;
    --white: #ffffff;
    --ink: #111111;
    --backdrop: #e9e4dc;
  }
  * { margin: 0; padding: 0; box-sizing: border-box; }
  html, body { width: 900px; height: 1200px; overflow: hidden; }
  body { background: var(--backdrop); position: relative; font-family: "Poppins", sans-serif; }

  .card {
    position: absolute; left: 80px; width: 733px; height: 428px;
    background: var(--white); border-radius: 22px; overflow: hidden;
    box-shadow: 0 6px 16px rgba(0,0,0,0.25);
  }
  .card--front { top: 130px; }
  .card--back { top: 646px; }

  /* front */
  .name-panel {
    position: absolute; left: 0; top: 0; width: 313px; height: 143px;
    background: var(--red); border-bottom-right-radius: 42px;
    padding: 46px 0 0 40px; color: var(--white);
    font-family: "Josefin Sans", sans-serif; font-weight: 600;
  }
  .name-panel .person { font-size: 26px; line-height: 1; letter-spacing: -0.2px; }
  .name-panel .role { font-size: 19px; margin-top: 6px; }
  .corner-dot { position: absolute; border-radius: 50%; background: var(--red); }
  .corner-dot--top { width: 130px; height: 130px; right: -65px; top: -65px; }
  .corner-dot--bottom { width: 120px; height: 120px; left: -55px; bottom: -70px; }

  .brand {
    position: absolute; display: flex; align-items: center; gap: 14px;
    font-family: "Josefin Sans", sans-serif; font-weight: 700; color: var(--ink);
  }
  .brand .mark { width: 26px; height: 26px; border-radius: 50%; background: var(--red); }
  .brand--front { left: 400px; top: 180px; font-size: 50px; }
  .brand--back { left: 78px; top: 256px; font-size: 56px; }

  .contact-list { position: absolute; left: 38px; top: 211px; list-style: none; }
  .contact-list li {
    display: flex; align-items: flex-start; gap: 12px;
    font-size: 16.5px; color: var(--ink); height: 40px; line-height: 26px;
  }
  .contact-list svg { flex: none; margin-top: 0; }
  .contact-list .address { line-height: 30px; margin-top: -2px; }

  .hours-panel {
    position: absolute; right: 0; bottom: 0; width: 391px; height: 144px;
    background: var(--black); border-top-left-radius: 36px;
    display: flex; align-items: center; padding: 10px 0 0 33px;
  }
  .hours-label {
    font-family: "Josefin Sans", sans-serif; font-weight: 600; color: var(--red);
    font-size: 17px; line-height: 25px; padding-right: 12px;
    border-right: 1.5px solid var(--white);
  }
  .hours-text { color: var(--white); font-size: 16.5px; line-height: 28px; padding-left: 14px; }

  /* back */
  .side-arc {
    position: absolute; width: 170px; height: 170px; border-radius: 50%;
    background: var(--black); left: -140px; top: 130px;
  }
  .service-disc {
    position: absolute; width: 520px; height: 520px; border-radius: 50%;
    background: var(--red); left: 425px; top: -45px;
  }
  .service-line {
    position: absolute; right: 43px; top: 158px; text-align: right;
    font-family: "Oswald", sans-serif; font-weight: 500; color: var(--white);
    font-size: 31px; line-height: 39px; text-transform: uppercase;
  }
</style>
</head>
<body>
  <section class="card card--front">
    <div class="name-panel">
      <div class="person">YOUR NAME HERE</div>
      <div class="role">OWNER</div>
    </div>
    <div class="corner-dot corner-dot--top"></div>
    <div class="corner-dot corner-dot--bottom"></div>

    <div class="brand brand--front"><span class="mark"></span>Tindlebox</div>

    <ul class="contact-list">
      <li>
        <svg width="26" height="26" viewBox="0 0 24 24"><circle cx="12" cy="12" r="10" fill="none" stroke="var(--red)" stroke-width="2.8"/><path d="M8.5 7.5l2 2-1 1.2a6 6 0 0 0 3.8 3.8l1.2-1 2 2-1.3 1.3c-3.5-.3-7.7-4.5-8-8z" fill="var(--red)"/></svg>
        <span>9094417382</span>
      </li>
      <li>
        <svg width="26" height="26" viewBox="0 0 24 24"><circle cx="12" cy="12" r="10" fill="none" stroke="var(--red)" stroke-width="2.8"/><rect x="7" y="8.5" width="10" height="7" fill="none" stroke="var(--red)" stroke-width="1.6"/><path d="M7 8.5l5 4 5-4" fill="none" stroke="var(--red)" stroke-width="1.6"/></svg>
        <span>info@Tindlebox.com</span>
      </li>
      <li>
        <svg width="26" height="26" viewBox="0 0 24 24"><circle cx="12" cy="12" r="10" fill="none" stroke="var(--red)" stroke-width="2.8"/><circle cx="12" cy="12" r="5" fill="none" stroke="var(--red)" stroke-width="1.5"/><path d="M7 12h10M12 7v10" stroke="var(--red)" stroke-width="1.3"/></svg>
        <span>Tindlebox.com</span>
      </li>
      <li>
        <svg width="26" height="26" viewBox="0 0 24 24"><circle cx="12" cy="12" r="10" fill="none" stroke="var(--red)" stroke-width="2.8"/><path d="M12 17.5s-4-4-4-7a4 4 0 0 1 8 0c0 3-4 7-4 7z" fill="var(--red)"/><circle cx="12" cy="10.5" r="1.5" fill="var(--white)"/></svg>
        <span class="address">457 Calloway Court Suite<br>B Cedar Hollow CA 92481</span>
      </li>
    </ul>

    <div class="hours-panel">
      <div class="hours-label">WORKING<br>HOURS</div>
      <div class="hours-text">M-F 9AM-5PM<br>Sat and Sun by Appointment</div>
    </div>
  </section>

  <section class="card card--back">
    <div class="side-arc"></div>
    <div class="service-disc"></div>
    <div class="brand brand--back"><span class="mark"></span>Tindlebox</div>
    <div class="service-line">All type of<br>mobile phone and<br>tablet repair</div>
  </section>
</body>
</html>
```